Design nice user interface for an MINDRA test website

I need you to design a modern user interface for MINDRA-test website. Questions and answers for the test are already known.

The test itself has all the questions in the form of an image where a portion of the image is cut off, and then the user has either 6 or 8 possible answers. The user needs to click one option to select his answer.

Proof of concept is here (you can find test questions there already):
https://vorpelin.org/projects/IQ-test/

I need only the design from you, no programming at all. The test questions are already given, you will not create your own questions/answers. Note that the images for test questions and answers (as shown at the URL) are not blue, they are transparent PNGs. So the background does not need to be blue.

While thinking about the design, consider adding nice progress bar (so user knows how many more questions to answer), and there needs to be also a time limit, which counts from 40:00 minutes down to zero.

Redesign for the actual questions/answer images is not required. If you decide to redesign the questions to make them nicer, you can do so, you may have higher chances to be selected as a winner, but keep in mind there are 60 questions in total, so it will be lot of additional work for you (feel free to suggest your idea).

Keep in mind that the design must be convertable to a "portrait mode" (eg. for devices where screen width is small)

Feel free to get as creative as you like.

So basically I would like to see at least 3 pages from you designed:
- some basic main page of the website with some lorem ipsum texts, and a "START TEST" button
- test page (where the test questions are displayed and answers are selected)
- a form page (after test is completed, user will enter name/email/age and click some button to get the test results emailed to him)

```html
<!DOCTYPE html>
<html lang="en">
<head>
<meta charset="utf-8">
<title>Mindra IQ Test</title>
<link rel="stylesheet" href="https://fonts.googleapis.com/css2?family=DM+Sans:wght@400;500;700&family=Roboto+Condensed:wght@300;400;700&family=Roboto:wght@300;400&display=swap">
<style>
:root{
  --ember:#c9472a;
  --ember-deep:#a83a2c;
  --violet:#3b2670;
  --indigo:#2d2a78;
  --royal:#3c4fd2;
  --action:#1f3ae6;
  --white:#ffffff;
  --ink:#2a3bd6;
  --line:rgba(255,255,255,.35);
  --glass:rgba(255,255,255,.12);
  --glow:#8a7bff;
}
*{box-sizing:border-box;margin:0;padding:0}
html,body{width:689px;height:1200px;overflow:hidden;background:var(--white)}
body{font-family:"DM Sans",Arial,sans-serif;color:var(--white)}
.stage{width:900px;height:1568px;transform:scale(.76556);transform-origin:0 0;position:relative;background:var(--white)}
.screen{position:absolute;left:0;width:900px;overflow:hidden;
  background:
    radial-gradient(circle at 105px 95px,rgba(200,70,40,.95) 0,rgba(200,70,40,.95) 108px,transparent 109px),
    radial-gradient(circle at 820px 470px,rgba(70,90,230,.55) 0,rgba(70,90,230,.55) 100px,transparent 101px),
    linear-gradient(115deg,var(--ember) 0%,#7a2f5a 30%,var(--violet) 55%,var(--indigo) 75%,var(--royal) 100%);}
.screen--home{top:0;height:520px}
.screen--test{top:543px;height:502px}
.screen--result{top:1065px;height:503px}

.topbar{position:absolute;left:0;top:0;width:100%;height:66px;border-bottom:1px solid var(--line)}
.brand{position:absolute;top:18px;font-family:"DM Sans",sans-serif;font-weight:700;font-size:24px;color:var(--white);display:flex;align-items:center;gap:7px}
.brand-dot{width:11px;height:11px;border-radius:50%;background:var(--white)}
.nav{position:absolute;left:314px;top:26px;display:flex;font-size:11px;letter-spacing:.3px}
.nav span{margin-right:20px}
.nav .sep{opacity:.9}
.pill{position:absolute;top:21px;width:100px;height:27px;border-radius:14px;font-size:11px;font-weight:700;display:flex;align-items:center;justify-content:center;gap:5px}
.pill--up{left:625px;background:var(--white);color:var(--ink)}
.pill--in{left:738px;background:var(--action);color:var(--white)}
.pill svg{width:11px;height:11px}

.rail{position:absolute;width:3px}
.rail i{display:block;width:3px;height:36px;margin-bottom:9px;border-radius:2px;background:rgba(255,255,255,.35)}
.rail i.on{background:var(--white)}

/* home */
.hero-kicker{position:absolute;left:47px;top:176px;font-family:"Roboto",sans-serif;font-weight:300;font-size:33px;letter-spacing:.5px}
.hero-title{position:absolute;left:47px;top:223px;font-family:"Roboto Condensed",sans-serif;font-weight:700;font-size:35px;letter-spacing:.8px}
.hero-copy{position:absolute;left:47px;top:277px;width:440px;font-size:10.5px;line-height:21px}
.btn-start{position:absolute;left:46px;top:357px;width:112px;height:31px;border-radius:16px;background:var(--white);color:var(--ink);font-size:10.5px;font-weight:700;display:flex;align-items:center;justify-content:center;letter-spacing:.3px}
.art-brain{position:absolute;left:520px;top:150px;width:350px;height:285px;border-radius:50%;
  background:radial-gradient(ellipse at 35% 40%,#ffb36a 0,#d56ce0 30%,#7b5cf0 55%,rgba(60,90,220,.3) 75%,transparent 78%)}

/* test */
.timer{position:absolute;left:411px;top:84px;width:75px;height:26px;background:var(--action);font-size:12px;font-weight:700;display:flex;align-items:center;justify-content:center}
.help{position:absolute;left:770px;top:88px;width:18px;height:18px;border-radius:50%;background:var(--white);color:#2a2a70;font-weight:700;font-size:13px;display:flex;align-items:center;justify-content:center}
.quiz{position:absolute;left:101px;top:128px;width:693px;height:270px;background:var(--glass)}
.quiz-head{position:absolute;left:0;top:0;width:100%;height:36px;border-bottom:1px solid var(--line);font-size:10px;font-weight:700}
.quiz-count{position:absolute;left:19px;top:14px}
.quiz-label{position:absolute;left:204px;top:5px;font-size:9.5px}
.progress{position:absolute;left:204px;top:18px;width:284px;height:4px;border-radius:2px;background:#cfcfe0}
.progress b{display:block;width:54px;height:4px;border-radius:2px;background:#9a1be0}
.quiz-skip{position:absolute;right:25px;top:14px}
.quiz-split{position:absolute;left:347px;top:36px;width:1px;height:234px;background:var(--line)}
.puzzle{position:absolute;left:27px;top:56px;width:294px;height:187px;border:2px solid #e9e6f5;background:linear-gradient(135deg,#6d5aa8,#5a4f9e)}
.choices{position:absolute;left:364px;top:70px;width:310px;display:grid;grid-template-columns:repeat(3,90px);column-gap:18px;row-gap:15px}
.choice{display:flex;flex-direction:column;align-items:center;gap:7px}
.choice-art{width:90px;height:52px;background:linear-gradient(135deg,#7e6cb6,#6a5cae)}
.choice-num{width:13px;height:13px;border-radius:50%;background:var(--action);font-size:8px;font-weight:700;display:flex;align-items:center;justify-content:center}
.choice-num.picked{background:var(--white);color:var(--ember);border:1.5px solid var(--ember)}
.glow{position:absolute;height:3px;border-radius:2px;background:linear-gradient(90deg,transparent,var(--glow),#fff,var(--glow),transparent)}
.step{position:absolute;top:415px;width:73px;height:30px;background:var(--white);color:var(--ink);font-size:10px;font-weight:700;display:flex;align-items:center;justify-content:center}

/* result */
.card{position:absolute;left:92px;top:96px;width:388px;height:362px;background:rgba(255,255,255,.18);border-radius:3px}
.card-title{position:absolute;left:0;top:20px;width:100%;text-align:center;font-family:"Roboto Condensed",sans-serif;font-weight:700;font-size:23px;letter-spacing:.6px}
.card-copy{position:absolute;left:14px;top:55px;width:360px;text-align:center;font-family:"Roboto",sans-serif;font-size:10px;line-height:20px;opacity:.9}
.socials{position:absolute;left:146px;top:104px;display:flex;gap:11px}
.socials i{width:25px;height:25px;border-radius:50%;background:rgba(255,255,255,.85)}
.or{position:absolute;left:12px;top:137px;width:364px;height:16px;font-size:8px;text-align:center}
.or::before{content:"";position:absolute;left:0;top:8px;width:100%;height:1px;background:var(--line)}
.or span{position:relative;padding:0 6px;background:#7a4f86}
.field-label{position:absolute;left:14px;font-family:"Roboto",sans-serif;font-size:10.5px}
.field{position:absolute;left:12px;width:365px;height:26px;border:1px solid rgba(255,255,255,.7);border-radius:3px;font-family:"Roboto",sans-serif;font-size:10.5px;display:flex;align-items:center}
.field-icon{width:31px;height:100%;border-right:1px solid rgba(255,255,255,.7);display:flex;align-items:center;justify-content:center}
.field-icon svg{width:11px;height:11px}
.field span{padding-left:9px}
.remember{position:absolute;left:26px;top:281px;font-size:11px;font-family:"Roboto",sans-serif;display:flex;align-items:center;gap:5px}
.remember i{width:7px;height:7px;background:var(--white)}
.forgot{position:absolute;right:18px;top:280px;font-size:11px;font-family:"Roboto",sans-serif}
.btn-login{position:absolute;left:12px;top:305px;width:82px;height:24px;background:linear-gradient(90deg,var(--ember-deep),#3d3fc8);font-family:"Roboto",sans-serif;font-size:10.5px;display:flex;align-items:center;justify-content:center}
.art-orb{position:absolute;left:575px;top:5px;width:320px;height:498px;
  background:linear-gradient(180deg,rgba(40,50,150,.6) 0%,#2f55d8 45%,#3a6ef0 70%,#2747c8 100%)}
</style>
</head>
<body>
<div class="stage">

  <section class="screen screen--home">
    <header class="topbar">
      <div class="brand" style="left:20px"><i class="brand-dot"></i>Mindra</div>
      <nav class="nav"><span>Home</span><span class="sep">|</span><span>About Us</span><span class="sep">|</span><span>Test</span><span class="sep">|</span><span>Contact Us</span></nav>
      <div class="pill pill--up"><svg viewBox="0 0 12 12"><path d="M1 2h4v1H2v6h3v1H1zM6 3l4 3-4 3V7H3V5h3z" fill="currentColor"/></svg>Sign Up</div>
      <div class="pill pill--in"><svg viewBox="0 0 12 12"><path d="M7 2h4v8H7V9h3V3H7zM1 5h4V3l3 3-3 3V7H1z" fill="currentColor"/></svg>Sign In</div>
    </header>
    <div class="rail" style="left:22px;top:195px"><i class="on"></i><i></i><i></i></div>
    <p class="hero-kicker">Lorem Ipsum is Simply</p>
    <h1 class="hero-title">Dummy Text of The Printing</h1>
    <p class="hero-copy">It is a long established fact that a reader will be distracted by the readable content of a page when looking at its layout. The point of using Lorem Ipsum is that it has a more-or-less</p>
    <div class="btn-start">START TEST</div>
    <div class="art-brain" role="img" aria-label="Glowing illustrated human brain in orange, pink and blue light"></div>
  </section>

  <section class="screen screen--test">
    <header class="topbar">
      <div class="brand" style="left:60px"><i class="brand-dot"></i>Mindra</div>
      <nav class="nav"><span>Home</span><span class="sep">|</span><span>About Us</span><span class="sep">|</span><span>Test</span><span class="sep">|</span><span>Contact Us</span></nav>
      <div class="pill pill--up"><svg viewBox="0 0 12 12"><path d="M1 2h4v1H2v6h3v1H1zM6 3l4 3-4 3V7H3V5h3z" fill="currentColor"/></svg>Sign Up</div>
      <div class="pill pill--in"><svg viewBox="0 0 12 12"><path d="M7 2h4v8H7V9h3V3H7zM1 5h4V3l3 3-3 3V7H1z" fill="currentColor"/></svg>Sign In</div>
    </header>
    <div class="rail" style="left:29px;top:195px"><i></i><i class="on"></i><i></i></div>
    <div class="timer">40:00</div>
    <div class="help">?</div>
    <div class="quiz">
      <div class="quiz-head">
        <span class="quiz-count">1/60</span>
        <span class="quiz-label">Question 1 / 60</span>
        <div class="progress"><b></b></div>
        <span class="quiz-skip">Skip &#8250;</span>
      </div>
      <div class="quiz-split"></div>
      <div class="puzzle" role="img" aria-label="Question pattern with a missing piece cut out"></div>
      <div class="choices">
        <div class="choice"><div class="choice-art" role="img" aria-label="Answer option 1 pattern"></div><span class="choice-num">1</span></div>
        <div class="choice"><div class="choice-art" role="img" aria-label="Answer option 2 pattern"></div><span class="choice-num picked">2</span></div>
        <div class="choice"><div class="choice-art" role="img" aria-label="Answer option 3 pattern"></div><span class="choice-num">3</span></div>
        <div class="choice"><div class="choice-art" role="img" aria-label="Answer option 4 pattern"></div><span class="choice-num">4</span></div>
        <div class="choice"><div class="choice-art" role="img" aria-label="Answer option 5 pattern"></div><span class="choice-num">5</span></div>
        <div class="choice"><div class="choice-art" role="img" aria-label="Answer option 6 pattern"></div><span class="choice-num">6</span></div>
      </div>
    </div>
    <div class="glow" style="left:200px;top:398px;width:500px"></div>
    <div class="step" style="left:368px">&#8249; PREVIOUS</div>
    <div class="step" style="left:451px">NEXT &#8250;</div>
  </section>

  <section class="screen screen--result">
    <div class="art-orb" role="img" aria-label="Illustrated blue brain floating in glowing rings above a round pedestal"></div>
    <header class="topbar">
      <div class="brand" style="left:60px"><i class="brand-dot"></i>Mindra</div>
      <nav class="nav"><span>Home</span><span class="sep">|</span><span>About Us</span><span class="sep">|</span><span>Test</span><span class="sep">|</span><span>Contact Us</span></nav>
      <div class="pill pill--up"><svg viewBox="0 0 12 12"><path d="M1 2h4v1H2v6h3v1H1zM6 3l4 3-4 3V7H3V5h3z" fill="currentColor"/></svg>Sign Up</div>
      <div class="pill pill--in"><svg viewBox="0 0 12 12"><path d="M7 2h4v8H7V9h3V3H7zM1 5h4V3l3 3-3 3V7H1z" fill="currentColor"/></svg>Sign In</div>
    </header>
    <div class="rail" style="left:22px;top:195px"><i></i><i></i><i class="on"></i></div>
    <div class="card">
      <h2 class="card-title">Sign In to View your Test Result</h2>
      <p class="card-copy">It is a long established fact that a reader will be distracted by the readable content of a page when looking at its layout.</p>
      <div class="socials"><i role="img" aria-label="Glint sign in"></i><i role="img" aria-label="Facet sign in"></i><i role="img" aria-label="Snapframe sign in"></i></div>
      <div class="or"><span>OR</span></div>
      <span class="field-label" style="top:165px">Email</span>
      <div class="field" style="top:186px"><span class="field-icon"><svg viewBox="0 0 12 12"><path d="M1 3h10v6H1zM1 3l5 4 5-4" fill="none" stroke="#fff"/></svg></span><span>Enter your Email ID</span></div>
      <span class="field-label" style="top:226px">Password</span>
      <div class="field" style="top:247px"><span class="field-icon"><svg viewBox="0 0 12 12"><rect x="2" y="5" width="8" height="6" fill="#fff"/><path d="M4 5V3a2 2 0 0 1 4 0v2" fill="none" stroke="#fff"/></svg></span><span>Enter your Password</span></div>
      <div class="remember"><i></i>Remember Me</div>
      <div class="forgot">Forgot Password <b>?</b></div>
      <div class="btn-login">LOGIN</div>
    </div>
    <div class="glow" style="left:140px;top:457px;width:290px"></div>
  </section>

</div>
</body>
</html>
```